RBT Fittings Ltd Business Cards

We need a business card with our business logo. We provide window and door installations on high-rises in west coast British Colombia, Canada.

I would like my business information and details on one side of the card, and the other side the company name with logo

Target Market(s)

General Contractors

Industry/Entity Type

Construction

Contact Information for Business Card

one side i want my company name and logo in the dark theme logo that i provided

Requirements
Must have
• Tomas Welbury, 16045518293, RBTFittings@mailvero.com, 1408-5192 Pemberly Avenue Burnaby BC, V6K 2R9, Owner & Manager

```html
<!DOCTYPE html>
<html lang="en">
<head>
<meta charset="utf-8">
<title>RBT Fittings Ltd – Business Cards</title>
<link href="https://fonts.googleapis.com/css2?family=Nunito:wght@500;700;800&display=swap" rel="stylesheet">
<style>
  :root {
    --page-bg: #ececec;
    --card-bg: #ffffff;
    --brand-blue: #29a9e1;
    --ink: #111111;
    --map-tint: #f1f4ec;
  }
  * { margin: 0; padding: 0; box-sizing: border-box; }
  html, body {
    width: 1200px;
    height: 1000px;
    overflow: hidden;
    background: var(--page-bg);
    font-family: "Nunito", sans-serif;
  }
  .canvas { position: relative; width: 1200px; height: 1000px; }

  .card {
    position: absolute;
    left: 233px;
    width: 733px;
    height: 418px;
    background: var(--card-bg);
    border-radius: 22px;
    overflow: hidden;
  }
  .card--front { top: 46px; }
  .card--back { top: 535px; }

  .world-map-area {
    position: absolute;
    left: 8px;
    top: 38px;
    width: 705px;
    height: 348px;
    background: radial-gradient(ellipse at center, var(--map-tint) 0%, var(--map-tint) 55%, rgba(241,244,236,0) 80%);
  }

  .brand {
    position: absolute;
    display: flex;
    align-items: center;
    gap: 12px;
    color: var(--brand-blue);
    font-weight: 800;
    white-space: nowrap;
    transform: translate(-50%, -50%);
  }
  .brand__mark { background: var(--brand-blue); flex: none; }
  .brand--front { left: 366px; top: 214px; font-size: 36px; }
  .brand--front .brand__mark { width: 40px; height: 40px; }
  .brand--back { left: 175px; top: 212px; font-size: 22px; gap: 8px; }
  .brand--back .brand__mark { width: 24px; height: 24px; }

  .title-bar {
    position: absolute;
    left: 364px;
    top: 0;
    width: 28px;
    height: 168px;
    background: var(--brand-blue);
  }
  .person { position: absolute; left: 414px; top: 72px; }
  .person__name { font-size: 36px; font-weight: 800; color: var(--ink); line-height: 1.1; white-space: nowrap; }
  .person__role {
    display: flex;
    align-items: center;
    gap: 6px;
    margin-top: 6px;
    font-size: 17px;
    font-weight: 500;
    color: var(--brand-blue);
    white-space: nowrap;
  }
  .person__role::after {
    content: "";
    width: 72px;
    height: 2px;
    background: var(--brand-blue);
    margin-top: 4px;
  }

  .contact-list { position: absolute; left: 364px; top: 193px; list-style: none; }
  .contact-list li {
    display: flex;
    align-items: center;
    gap: 21px;
    min-height: 36px;
    margin-bottom: 14px;
    font-size: 21px;
    font-weight: 500;
    color: var(--ink);
    white-space: nowrap;
  }
  .contact-list .contact-address {
    font-size: 16px;
    line-height: 19px;
  }
  .contact-icon {
    width: 27px;
    height: 36px;
    display: flex;
    align-items: center;
    justify-content: center;
    background: var(--ink);
    flex: none;
  }
  .contact-icon--blue { background: var(--brand-blue); }
  .contact-icon svg { width: 17px; height: 17px; }

  .bottom-band {
    position: absolute;
    left: 0;
    bottom: 0;
    width: 100%;
    height: 9px;
    background: var(--brand-blue);
  }
</style>
</head>
<body>
<div class="canvas">

  <section class="card card--front">
    <div class="world-map-area" role="img" aria-label="Faint world map in the background"></div>
    <div class="brand brand--front">
      <span class="brand__mark"></span>
      <span class="brand__name">RBT Fittings Ltd</span>
    </div>
  </section>

  <section class="card card--back">
    <div class="brand brand--back">
      <span class="brand__mark"></span>
      <span class="brand__name">RBT Fittings Ltd</span>
    </div>

    <div class="title-bar"></div>
    <div class="person">
      <p class="person__name">Tomas Welbury</p>
      <p class="person__role">Owner &amp; Manager</p>
    </div>

    <ul class="contact-list">
      <li>
        <span class="contact-icon">
          <svg viewBox="0 0 24 24" fill="none" stroke="#fff" stroke-width="1.8" stroke-linecap="round" stroke-linejoin="round"><path d="M5 3h4l2 5-2.5 1.5a11 11 0 0 0 6 6L16 13l5 2v4a2 2 0 0 1-2 2A16 16 0 0 1 3 5a2 2 0 0 1 2-2z"/></svg>
        </span>
        <span>16045518293</span>
      </li>
      <li>
        <span class="contact-icon contact-icon--blue">
          <svg viewBox="0 0 24 24" fill="none" stroke="#fff" stroke-width="1.8" stroke-linejoin="round"><rect x="3" y="6" width="18" height="12"/><path d="M3 6l9 7 9-7"/></svg>
        </span>
        <span>RBTFittings@mailvero.com</span>
      </li>
      <li>
        <span class="contact-icon">
          <svg viewBox="0 0 24 24" fill="none" stroke="#fff" stroke-width="1.6"><circle cx="12" cy="12" r="9"/><ellipse cx="12" cy="12" rx="4" ry="9"/><path d="M3 12h18M5 7h14M5 17h14"/></svg>
        </span>
        <span>www.rbtfittings.example</span>
      </li>
      <li>
        <span class="contact-icon contact-icon--blue">
          <svg viewBox="0 0 24 24" fill="none" stroke="#fff" stroke-width="1.8" stroke-linejoin="round"><path d="M12 21s-7-6.5-7-12a7 7 0 0 1 14 0c0 5.5-7 12-7 12z"/><circle cx="12" cy="9" r="2.5"/></svg>
        </span>
        <span class="contact-address">1408-5192 Pemberly Avenue<br>Burnaby BC, V6K 2R9</span>
      </li>
    </ul>

    <div class="bottom-band"></div>
  </section>

</div>
</body>
</html>
```